GUARANTEE PAY GIFT CARD DESIGN

This is a GIFT BONUS CARD

SIZE: 3.5INCH x 2INCH, 8.9cm x 5.1cm, DOUBLE SIDE
Orange must be used as an accent or primary colour.
#F37021, CMYK 0, 54, 86, 5

"BONUS CARD" AND "$20" MUST BE PART OF THE DESIGN.

Please see the attached logo
DO NOT use ribbons or gift box illustrations in the design.

***Terms and conditions must be on the back side of the card-
"No Cash Value. Card valid from 1/2/2024 to 3/31/2024. Valid for Katy location only. Valid for Dine-in only. Not valid for online togo, delivery, or special events. "

Target Market(s)

40-60 YEARS OLD

Industry/Entity Type

Modern casual malaysian restaurant

Requirements
Must have
• ORANGE COLOUR, BONUS CARD, $20
Should not have
• Ribbons, gift box, CHOPSTICKS, BOWL, NOODLES, CHARATER ILLUSTRATIONS.

```html
<!DOCTYPE html>
<html lang="en">
<head>
<meta charset="UTF-8">
<title>Kaya House Bonus Card</title>
<link rel="stylesheet" href="https://fonts.googleapis.com/css2?family=Josefin+Sans:wght@400;500;600;700&display=swap">
<style>
  :root {
    --backdrop: #d8d5d2;
    --orange: #f0922f;
    --orange-light: #f39a36;
    --orange-deep: #e2852c;
    --wave-dark: #c9701f;
    --ink: #121212;
    --band: #0f0f0f;
    --cream: #fdf2e2;
    --white: #ffffff;
  }
  * { margin: 0; padding: 0; box-sizing: border-box; }
  html, body {
    width: 1200px;
    height: 1200px;
    overflow: hidden;
    background: var(--backdrop);
    font-family: "Josefin Sans", sans-serif;
  }
  .canvas {
    position: relative;
    width: 1200px;
    height: 1200px;
  }
  .card {
    position: absolute;
    left: 243px;
    width: 702px;
    height: 400px;
    border-radius: 24px;
    overflow: hidden;
    box-shadow: 0 10px 22px rgba(0, 0, 0, 0.22);
  }
  .card--front { top: 170px; }
  .card--back {
    top: 630px;
    background: linear-gradient(160deg, var(--orange-light), var(--orange-deep));
    text-align: center;
    color: var(--ink);
  }

  /* Front */
  .front-pattern {
    position: absolute;
    left: 0; top: 0;
    width: 100%;
    height: 318px;
    background: linear-gradient(135deg, var(--orange-light) 0%, var(--orange) 55%, var(--wave-dark) 100%);
  }
  .brand-mark {
    position: absolute;
    left: 349px;
    top: 159px;
    transform: translate(-50%, -50%);
    font-weight: 500;
    font-size: 32px;
    letter-spacing: 3px;
    color: var(--ink);
    white-space: nowrap;
  }
  .terms-note {
    position: absolute;
    left: 685px;
    top: 160px;
    transform: translate(-50%, -50%) rotate(-90deg);
    font-size: 10px;
    color: var(--ink);
    white-space: nowrap;
  }
  .front-band {
    position: absolute;
    left: 0; bottom: 0;
    width: 100%;
    height: 82px;
    background: var(--band);
  }
  .card-label {
    position: absolute;
    left: 35px;
    top: 32px;
    font-size: 22px;
    font-weight: 500;
    letter-spacing: 1px;
    color: var(--white);
  }
  .card-value {
    position: absolute;
    left: 581px;
    top: 14px;
    width: 81px;
    height: 50px;
    border: 2px solid var(--orange);
    border-radius: 8px;
    color: var(--white);
    font-size: 30px;
    font-weight: 600;
    display: flex;
    align-items: center;
    justify-content: center;
    padding-top: 5px;
  }
  .card-value sup {
    font-size: 14px;
    margin-right: 1px;
    align-self: flex-start;
    margin-top: 4px;
  }

  /* Back */
  .back-brand {
    margin-top: 52px;
    font-size: 32px;
    font-weight: 500;
    letter-spacing: 3px;
  }
  .back-rule {
    width: 115px;
    height: 1px;
    margin: 22px auto 0;
    background: var(--ink);
  }
  .terms-heading {
    margin-top: 22px;
    font-size: 16px;
    font-weight: 400;
    color: var(--cream);
  }
  .terms-list {
    list-style: none;
    margin-top: 14px;
    font-size: 12.5px;
    line-height: 23px;
  }
</style>
</head>
<body>
<main class="canvas">

  <section class="card card--front" aria-label="Bonus card front">
    <div class="front-pattern" role="img" aria-label="Flowing diagonal wave line pattern in orange and bronze tones"></div>
    <div class="brand-mark">KAYA HOUSE</div>
    <p class="terms-note">Terms and Conditions apply</p>
    <div class="front-band">
      <span class="card-label">BONUS CARD</span>
      <span class="card-value"><sup>$</sup>20</span>
    </div>
  </section>

  <section class="card card--back" aria-label="Bonus card back">
    <div class="back-brand">KAYA HOUSE</div>
    <div class="back-rule"></div>
    <h2 class="terms-heading">Terms and Conditions</h2>
    <ul class="terms-list">
      <li>$20 Bonus Card valid from 1/2/2024 – 3/31/2024.</li>
      <li>$20 Bonus Card has no cash value and cannot be redeemed for cash or gift cards.</li>
      <li>No change returned with purchase of less than $20.</li>
      <li>$20 Bonus Card is not valid with any other coupons or promotional offer.</li>
      <li>Bonus Card is only valid for dine-in only.</li>
      <li>Bonus Card will not be replaced if lost, stolen, or damaged.</li>
      <li>Not valid for online to-go, delivery, or special events.</li>
      <li>Use of Bonus Card constitutes acceptance of these terms.</li>
    </ul>
  </section>

</main>
</body>
</html>
```